Boutique Shoe Bag Race wear Business Card Design

We are a new luxury shoe bag, jewellery and race wear store stocking local and international designers. Located in the fashion precinct of beautiful Calloway Cove famous in Sydney Australia. Stocking French jewellery and shoes such as Maximilien verdacs plus Australian made. Looking at quality and service and looking after the locals and tourists.
Ideas: White background, Black writing in bold engravers, logo in middle of Bondi and Boutique a gold horseshoe (facing upright so the curve is at the bottom) with a black stiletto inside. French clover silver and black border (not irish clover the French lattice type look)

Larkspur Parlour

I open 8/4 so require business card design ASAP.

Please place gold horseshoe facing upwards with the black stiletto inside.

Bold engravers writing for business name.

I will have my phone number tomorrow to update.

Border in similar/same style as attached picture with black/silver clover French design.

Thank you. Petra                                   

Industry/Entity Type

Fashion

Contact Information for Business Card

Larkspur Parlour
Boutique Owner Petra Halvorsen
41B Tindle Road
Calloway Cove WRN 4417 Australia
0491237406
07 **** *TBC
info@larkspurparlour.com.au
Facebook.com/LarkspurParlour
www.larkspurparlour.com.au

Font styles to use
Other font styles liked:
• Bold Engravers

Requirements
Must have
• Info on one side including business name and logo with black stiletto and gold horse shoe. reverse side with French clover border and Larger name Larkspur Parlour with logo in centre.
Should not have
• irish clover
French script
horseshoe upside down

```html
<!DOCTYPE html>
<html lang="en">
<head>
<meta charset="utf-8">
<title>Larkspur Parlour – Business Card</title>
<link rel="stylesheet" href="https://fonts.googleapis.com/css2?family=Cinzel:wght@700&family=Crimson+Text:ital,wght@0,400;1,400&family=Open+Sans:wght@400&display=swap">
<style>
  :root {
    --stage: #151515;
    --card: #ffffff;
    --gold: #b5a534;
    --ink: #231f20;
    --grey-text: #5a5a5a;
    --rule: #c8c8c8;
    --label: #ffffff;
    --ornament-line: #231f20;
    --ornament-fill: #f1f1f1;
  }
  * { box-sizing: border-box; margin: 0; padding: 0; }
  html, body { width: 900px; height: 1200px; overflow: hidden; }
  body { background: var(--stage); position: relative; font-family: "Crimson Text", Georgia, serif; }

  .card { position: absolute; background: var(--card); }
  .card--front { left: 45px; top: 43px; width: 815px; height: 505px; }
  .card--back  { left: 47px; top: 624px; width: 811px; height: 500px; }

  .side-label {
    position: absolute; color: var(--label);
    font-family: "Open Sans", Arial, sans-serif; font-size: 16px;
  }
  .side-label--front { left: 46px; top: 559px; }
  .side-label--back  { left: 48px; top: 1139px; }

  .owner-name {
    position: absolute; left: 62px; top: 68px;
    font-family: "Cinzel", "Times New Roman", serif; font-weight: 700;
    color: var(--gold); font-size: 48px; line-height: 1; letter-spacing: 4px;
    white-space: nowrap;
  }
  .owner-name .small { font-size: 37px; }
  .owner-rule {
    position: absolute; left: 62px; top: 125px; width: 616px; height: 1px; background: var(--rule);
  }
  .owner-role {
    position: absolute; left: 64px; top: 130px;
    font-style: italic; font-size: 18px; letter-spacing: 2px; color: var(--grey-text);
    white-space: nowrap;
  }
  .address {
    position: absolute; left: 64px; top: 180px;
    font-size: 20px; line-height: 24.5px; color: var(--grey-text); letter-spacing: 0.4px;
  }
  .brand-dot {
    position: absolute; left: 407px; top: 387px; width: 44px; height: 44px;
    border-radius: 50%; background: var(--gold);
  }
  .online {
    position: absolute; left: 483px; top: 373px;
    font-size: 19px; line-height: 25px; color: var(--grey-text); letter-spacing: 0.3px;
    white-space: nowrap;
  }

  .clover-tile { position: absolute; width: 74px; height: 74px; }
  .card--front .clover-tile { left: 675px; top: 89px; }

  .border-rule { position: absolute; height: 1px; background: var(--rule); left: 105px; width: 608px; }
  .border-rule--top { top: 65px; }
  .border-rule--bottom { top: 431px; }
  .clover-tile--tl { left: 33px; top: 28px; }
  .clover-tile--tr { left: 710px; top: 28px; }
  .clover-tile--bl { left: 33px; top: 394px; }
  .clover-tile--br { left: 710px; top: 394px; }

  .wordmark {
    position: absolute; left: 0; right: 0; top: 214px;
    display: flex; align-items: center; justify-content: center; gap: 18px;
    font-family: "Cinzel", "Times New Roman", serif; font-weight: 700;
    color: var(--ink); font-size: 38px; letter-spacing: 4px;
  }
  .wordmark .brand-dot--center {
    width: 78px; height: 78px; border-radius: 50%; background: var(--gold); flex: none;
  }
</style>
</head>
<body>

  <section class="card card--front">
    <h1 class="owner-name">P<span class="small">ETRA</span> H<span class="small">ALVORSEN</span></h1>
    <div class="owner-rule"></div>
    <p class="owner-role">Larkspur Parlour Boutique Owner</p>
    <p class="address">
      41B Tindle Road Calloway Cove<br>
      WRN 4417 Australia<br>
      0491237406<br>
      07 **** *TBC
    </p>
    <svg class="clover-tile" viewBox="0 0 74 74" role="img" aria-label="French clover ornament in a diamond frame">
      <polygon points="37,1 73,37 37,73 1,37" fill="var(--card)" stroke="var(--ornament-line)" stroke-width="1.2"/>
      <polygon points="37,19 55,37 37,55 19,37" fill="var(--ornament-fill)"/>
    </svg>
    <div class="brand-dot"></div>
    <p class="online">
      info@larkspurparlour.com.au<br>
      Facebook.com/LarkspurParlour<br>
      www.larkspurparlour.com.au
    </p>
  </section>
  <p class="side-label side-label--front">Front side</p>

  <section class="card card--back">
    <div class="border-rule border-rule--top"></div>
    <div class="border-rule border-rule--bottom"></div>
    <svg class="clover-tile clover-tile--tl" viewBox="0 0 74 74" role="img" aria-label="French clover ornament in a diamond frame">
      <polygon points="37,1 73,37 37,73 1,37" fill="var(--card)" stroke="var(--ornament-line)" stroke-width="1.2"/>
      <polygon points="37,19 55,37 37,55 19,37" fill="var(--ornament-fill)"/>
    </svg>
    <svg class="clover-tile clover-tile--tr" viewBox="0 0 74 74" role="img" aria-label="French clover ornament in a diamond frame">
      <polygon points="37,1 73,37 37,73 1,37" fill="var(--card)" stroke="var(--ornament-line)" stroke-width="1.2"/>
      <polygon points="37,19 55,37 37,55 19,37" fill="var(--ornament-fill)"/>
    </svg>
    <svg class="clover-tile clover-tile--bl" viewBox="0 0 74 74" role="img" aria-label="French clover ornament in a diamond frame">
      <polygon points="37,1 73,37 37,73 1,37" fill="var(--card)" stroke="var(--ornament-line)" stroke-width="1.2"/>
      <polygon points="37,19 55,37 37,55 19,37" fill="var(--ornament-fill)"/>
    </svg>
    <svg class="clover-tile clover-tile--br" viewBox="0 0 74 74" role="img" aria-label="French clover ornament in a diamond frame">
      <polygon points="37,1 73,37 37,73 1,37" fill="var(--card)" stroke="var(--ornament-line)" stroke-width="1.2"/>
      <polygon points="37,19 55,37 37,55 19,37" fill="var(--ornament-fill)"/>
    </svg>
    <div class="wordmark">
      <span>LARKSPUR</span>
      <span class="brand-dot--center"></span>
      <span>PARLOUR</span>
    </div>
  </section>
  <p class="side-label side-label--back">Back side</p>

</body>
</html>
```